Wendorf Legal: Sole Practitioner Law Firm seeking corporate branding drawing on unique bush setting

I need a logo, stationary and business card design for my law firm. I will be practising as a sole practitioner specialising in corporate, commercial, finance, migration and agriculture law. Having left my corporate job in the city and relocated our family to our farm in regional Western Australia, I would like the corporate design for my company to be crisp, stylish, concise and uncomplicated. The law firm is called "Wendorf Legal" because we have a colony of the endangered Carnaby Black Cockatoos living in the bush behind our homestead (which is also my office). I will travel to clients rather than have them visit me. I would like to see a stylised image of the bird with some Australian native bush included in the design, either as a background image on the back of the card. A separate brief has been created for the logo and stationary though I hope all 3 pieces of work will "marry". The final design should communicate clarity of vision, efficiency, compassion and solution/ outcome focused. I prefer to have the business cards printed on card with a bit of texture and substance. I will try not to use laminated card as I consider it feels "plastic and commoditised" which is inconsistent with the image and feel of the business I intend creating. Please see attached brief for further details of the design brief.

Target Market(s)

Agriculture and Horticulture companies, Farmers, Family offices and estates, banks, insurance companies, individuals wishing to migrate to Australia

Industry/Entity Type

Legal

Contact Information for Business Card

Harriet Dunbar-Kelso
LLB (Hons), BSc., MEc.
Legal Practitioner and Director

WENDORF LEGAL PTY LTD
PO Box 273, Yarrowind WA 6057
Ph: 0472 918205
Email: harrietdk@quillnet.com

Solicitor admitted to practice in the Senior Bench Tribunal of Western Australia, England and Wales, NSW, and Registered Practitioner of the Apex Bench of Australia

Logo Text

WENDORF LEGAL: Client Focused Commercial Legal Solutions

Font styles to use
Other font styles liked:
• Verlag

Colors
ec1f27
fbee3d
9bcb3c
ffffff
1b1b1b
c4c4c4

Requirements
Must have
• A look and feel of quality, conservatism, adventure
Nice to have
• A stylised image of a Carnaby Cockatoo and Australian flora as a background image or design on the back of the card.
Should not have
• Clutter, cartoons

```html
<!DOCTYPE html>
<html lang="en">
<head>
<meta charset="utf-8">
<title>Wendorf Legal — Business Card and Logo</title>
<link rel="stylesheet" href="https://fonts.googleapis.com/css2?family=Cinzel:wght@400&family=Source+Sans+3:wght@400;600&display=swap">
<style>
  :root {
    --gold: #f6b02c;
    --charcoal: #2b2b2b;
    --ink: #1b1b1b;
    --silver: #c4c4c4;
    --steel: #8d8d8d;
    --paper: #ffffff;
    --stage: #ebe7e1;
    --text-grey: #4a4a4a;
  }
  * { box-sizing: border-box; margin: 0; padding: 0; }
  html, body { width: 1200px; height: 945px; overflow: hidden; background: var(--paper); }
  .canvas { position: relative; width: 1200px; height: 945px; }

  .card-stage {
    position: absolute; left: 0; top: 0; width: 1200px; height: 688px;
    background: var(--stage);
  }
  .card {
    position: absolute; top: 219px; width: 440px; height: 251px;
    border-radius: 14px; box-shadow: 0 10px 24px rgba(0,0,0,.18);
  }
  .card--back { left: 130px; background: var(--charcoal); }
  .card--front { left: 630px; background: var(--paper); }

  .mark { position: absolute; border-radius: 50%; }
  .card--back .mark { left: 56px; top: 90px; width: 72px; height: 72px; background: var(--gold); }
  .card--back .company {
    position: absolute; left: 146px; top: 112px;
    font-family: "Cinzel", serif; font-size: 21px; letter-spacing: 1px; color: var(--silver);
  }

  .holder { position: absolute; left: 28px; top: 28px; font-family: "Source Sans 3", sans-serif; }
  .holder__name { font-size: 22px; color: var(--ink); }
  .holder__quals { font-size: 12px; color: var(--text-grey); margin-left: 4px; }
  .holder__role { font-size: 13px; color: var(--text-grey); margin-top: 2px; }

  .contact { position: absolute; left: 28px; bottom: 22px; list-style: none;
    font-family: "Source Sans 3", sans-serif; font-size: 12.5px; color: var(--text-grey); }
  .contact li { display: flex; align-items: center; gap: 8px; margin-top: 4px; }
  .contact svg { width: 11px; height: 11px; fill: var(--text-grey); flex: none; }

  .card--front .mark { left: 246px; top: 118px; width: 40px; height: 40px; background: var(--ink); }
  .card--front .company {
    position: absolute; left: 294px; top: 131px;
    font-family: "Cinzel", serif; font-size: 11px; color: var(--steel); white-space: nowrap;
  }

  .lockup { position: absolute; top: 764px; display: flex; align-items: center; gap: 14px; }
  .lockup--gold { left: 51px; }
  .lockup--black { left: 646px; }
  .lockup .mark { position: static; width: 128px; height: 128px; }
  .lockup--gold .mark { background: var(--gold); }
  .lockup--black .mark { background: var(--ink); }
  .lockup .company {
    font-family: "Cinzel", serif; font-size: 29px; letter-spacing: 1px; color: var(--charcoal); white-space: nowrap;
  }
</style>
</head>
<body>
<main class="canvas">
  <section class="card-stage">
    <article class="card card--back">
      <span class="mark"></span>
      <span class="company">WENDORF LEGAL PTY LTD</span>
    </article>

    <article class="card card--front">
      <div class="holder">
        <p><span class="holder__name">Harriet Dunbar-Kelso</span><span class="holder__quals">LLB (Hons), BSc., MEc.</span></p>
        <p class="holder__role">Legal Practitioner and Director</p>
      </div>
      <span class="mark"></span>
      <span class="company">WENDORF LEGAL PTY LTD</span>
      <ul class="contact">
        <li><svg viewBox="0 0 12 12"><path d="M6 0a4 4 0 0 0-4 4c0 3 4 8 4 8s4-5 4-8a4 4 0 0 0-4-4zm0 5.6A1.6 1.6 0 1 1 6 2.4a1.6 1.6 0 0 1 0 3.2z"/></svg>PO Box 273, Yarrowind WA 6057</li>
        <li><svg viewBox="0 0 12 12"><path d="M2.4 0.5l2 2.6-1.1 1.4a7 7 0 0 0 4.2 4.2l1.4-1.1 2.6 2-1.2 1.9C5.6 11.5 0.5 6.4 0.5 1.7z"/></svg>0472 918205</li>
        <li><svg viewBox="0 0 12 12"><path d="M0 2h12v8H0zM1 3l5 3.6L11 3v-.2H1z" fill-rule="evenodd"/></svg>harrietdk@quillnet.com</li>
      </ul>
    </article>
  </section>

  <div class="lockup lockup--gold">
    <span class="mark"></span>
    <span class="company">WENDORF LEGAL PTY LTD</span>
  </div>
  <div class="lockup lockup--black">
    <span class="mark"></span>
    <span class="company">WENDORF LEGAL PTY LTD</span>
  </div>
</main>
</body>
</html>
```